Business Card and Stationary Design

After the successful redesign of our logo we are wanting to follow suite and create a new business card and stationary design!

New Logo is attached, information required on the business card should contain a mixture of the following but layout/arrangement is up to the designer.

Happy if the national provider number and abn are on the back, and happy for them to be smaller than the rest.

I am also happy to receive single sided or weird and wonderful designs.

Name
Title
National Provider Number 7192
ABN 53 614 289 117
Level 1, 214 Garrow Street
Brackenvale NSW 2319
Ph: 1300 587 902
Mobile: 0438 761 205
name@ironquillbuild.com.au
www.ironquillbuild.com.au

Target Market(s)

Professionals, Peers, Students, Suppliers...

Industry/Entity Type

Construction

Contact Information for Business Card

Listed in project description

Font styles to use
Other font styles liked:
• Century Gothic

Colors
0455a3
3176b5
ffffff

Requirements
Must have
• Professional Design, same color scheme as our logo
Nice to have
• Something that sets our apart from everyone else would be fantastic, open to size and shape and layout options, as long as they present professionally.
• Open to raised/embossed text, alternative materials, custom sizes, clear material
Should not have
• The color orange

```html
<!DOCTYPE html>
<html lang="en">
<head>
<meta charset="utf-8">
<title>Ironquill Build – Business Card</title>
<link href="https://fonts.googleapis.com/css2?family=Questrial&display=swap" rel="stylesheet">
<style>
  :root {
    --backdrop: #6e6e6e;
    --paper: #ffffff;
    --ink-black: #050505;
    --brand-navy: #1f3b8a;
    --blue-1: #0b55a3;
    --blue-2: #2a73b6;
    --blue-3: #2f84c6;
    --blue-4: #3fa1db;
    --blue-5: #56b8e9;
    --blue-6: #66c8f0;
    --cell-1: #0b0b0b;
    --cell-2: #171717;
    --cell-3: #232323;
    --cell-4: #2f2f2f;
    --cell-5: #3c3c3c;
    --cell-6: #4a4a4a;
  }
  * { box-sizing: border-box; margin: 0; padding: 0; }
  html, body { width: 1200px; height: 1200px; overflow: hidden; }
  body {
    background: var(--backdrop);
    font-family: "Questrial", "Century Gothic", sans-serif;
    position: relative;
  }
  .card {
    position: absolute;
    left: 150px;
    width: 900px;
    height: 514px;
    overflow: hidden;
    box-shadow: 0 12px 30px rgba(0,0,0,.35);
  }
  .card--front { top: 60px; background: var(--paper); }
  .card--back { top: 626px; background: var(--ink-black); display: flex; }

  /* stepped accent bars */
  .step-bar { display: flex; position: absolute; }
  .step-bar span { flex: 1; }
  .step-bar span:nth-child(1) { background: var(--blue-1); }
  .step-bar span:nth-child(2) { background: var(--blue-2); }
  .step-bar span:nth-child(3) { background: var(--blue-3); }
  .step-bar span:nth-child(4) { background: var(--blue-4); }
  .step-bar span:nth-child(5) { background: var(--blue-5); }
  .step-bar span:nth-child(6) { background: var(--blue-6); }
  .step-bar--top { top: 0; left: 255px; width: 250px; height: 16px; }
  .step-bar--side { top: 0; right: 0; width: 20px; height: 240px; flex-direction: column; }

  /* wordmark */
  .wordmark { display: flex; align-items: center; gap: 16px; white-space: nowrap; }
  .wordmark__square { width: 34px; height: 34px; background: var(--brand-navy); }
  .wordmark__name { font-size: 64px; color: var(--brand-navy); letter-spacing: 1px; line-height: 1; }
  .card--front .wordmark { position: absolute; left: 195px; top: 190px; }
  .card--back .wordmark { position: absolute; left: 560px; top: 215px; gap: 10px; }
  .card--back .wordmark__square { width: 18px; height: 18px; background: var(--paper); }
  .card--back .wordmark__name { font-size: 31px; color: var(--paper); }

  .registration {
    position: absolute; left: 360px; top: 360px;
    font-size: 19px; color: #111; line-height: 1.35; text-align: center;
  }

  /* back contact panel */
  .contact { width: 500px; flex: none; display: grid; grid-template-columns: 80px 1fr; grid-template-rows: 84px 110px 80px 80px 80px 80px; }
  .contact__icon { display: flex; align-items: center; justify-content: center; }
  .contact__icon svg { width: 26px; height: 26px; fill: #fff; }
  .contact__text {
    display: flex; flex-direction: column; justify-content: center;
    padding-left: 40px; color: #fff; font-size: 25px; line-height: 1.25; white-space: nowrap;
  }
  .row-1.contact__icon { background: var(--cell-1); } .row-1.contact__text { background: var(--blue-1); font-size: 28px; }
  .row-2.contact__icon { background: var(--cell-2); } .row-2.contact__text { background: var(--blue-2); }
  .row-3.contact__icon { background: var(--cell-3); } .row-3.contact__text { background: var(--blue-3); }
  .row-4.contact__icon { background: var(--cell-4); } .row-4.contact__text { background: var(--blue-4); }
  .row-5.contact__icon { background: var(--cell-5); } .row-5.contact__text { background: var(--blue-5); font-size: 23px; }
  .row-6.contact__icon { background: var(--cell-6); } .row-6.contact__text { background: var(--blue-6); font-size: 23px; }
</style>
</head>
<body>

<section class="card card--front" aria-label="Card front">
  <div class="step-bar step-bar--top"><span></span><span></span><span></span><span></span><span></span><span></span></div>
  <div class="wordmark">
    <span class="wordmark__square"></span>
    <span class="wordmark__name">Ironquill Build</span>
  </div>
  <p class="registration">National Provider Number 7192<br>ABN 53 614 289 117</p>
</section>

<section class="card card--back" aria-label="Card back">
  <div class="contact">
    <div class="contact__icon row-1"><svg viewBox="0 0 24 24"><circle cx="12" cy="7" r="5"/><path d="M2 22c0-6 4.5-9 10-9s10 3 10 9z"/></svg></div>
    <div class="contact__text row-1">Name</div>

    <div class="contact__icon row-2"><svg viewBox="0 0 24 24"><path d="M12 1a8 8 0 0 0-8 8c0 6 8 14 8 14s8-8 8-14a8 8 0 0 0-8-8zm0 11a3 3 0 1 1 0-6 3 3 0 0 1 0 6z"/></svg></div>
    <div class="contact__text row-2"><span>Level 1, 214 Garrow Street</span><span>Brackenvale NSW 2319</span></div>

    <div class="contact__icon row-3"><svg viewBox="0 0 24 24"><path d="M6.6 10.8a15 15 0 0 0 6.6 6.6l2.2-2.2c.3-.3.7-.4 1-.2 1.1.4 2.3.6 3.6.6.6 0 1 .4 1 1V20c0 .6-.4 1-1 1A17 17 0 0 1 3 4c0-.6.4-1 1-1h3.5c.6 0 1 .4 1 1 0 1.3.2 2.5.6 3.6.1.3 0 .7-.2 1z"/></svg></div>
    <div class="contact__text row-3">1300 587 902</div>

    <div class="contact__icon row-4"><svg viewBox="0 0 24 24"><path d="M7 1h10a2 2 0 0 1 2 2v18a2 2 0 0 1-2 2H7a2 2 0 0 1-2-2V3a2 2 0 0 1 2-2zm0 3v14h10V4zm5 15.5a1 1 0 1 0 0 2 1 1 0 0 0 0-2z"/></svg></div>
    <div class="contact__text row-4">0438 761 205</div>

    <div class="contact__icon row-5"><svg viewBox="0 0 24 24"><path d="M2 5h20v14H2zm2 2v.5l8 5 8-5V7zm0 2.8V17h16V9.8l-8 5z"/></svg></div>
    <div class="contact__text row-5">name@ironquillbuild.com.au</div>

    <div class="contact__icon row-6"><svg viewBox="0 0 24 24"><path d="M12 2a10 10 0 1 0 0 20 10 10 0 0 0 0-20zm6.9 6h-3a15 15 0 0 0-1.3-3.9A8 8 0 0 1 18.9 8zM12 4c.8 1.2 1.5 2.5 1.9 4h-3.8c.4-1.5 1.1-2.8 1.9-4zM4.3 14a8 8 0 0 1 0-4h3.4a16 16 0 0 0 0 4zm.8 2h3a15 15 0 0 0 1.3 3.9A8 8 0 0 1 5.1 16zm3-8h-3a8 8 0 0 1 4.3-3.9A15 15 0 0 0 8.1 8zM12 20c-.8-1.2-1.5-2.5-1.9-4h3.8c-.4 1.5-1.1 2.8-1.9 4zm2.3-6H9.7a14 14 0 0 1 0-4h4.6a14 14 0 0 1 0 4zm.3 5.9a15 15 0 0 0 1.3-3.9h3a8 8 0 0 1-4.3 3.9zm1.7-5.9a16 16 0 0 0 0-4h3.4a8 8 0 0 1 0 4z"/></svg></div>
    <div class="contact__text row-6">www.ironquillbuild.com.au</div>
  </div>
  <div class="wordmark">
    <span class="wordmark__square"></span>
    <span class="wordmark__name">Ironquill Build</span>
  </div>
  <div class="step-bar step-bar--side"><span></span><span></span><span></span><span></span><span></span><span></span></div>
</section>

</body>
</html>
```